Tolvane Air and Electrical Website

Simple and easy to use website for a Electrical and Air Conditioning contracting business.Use stock photosOnline contact portallogo still to be supplied

Target Market(s)

Mums and Dads who want a local contractor

Coding

Coded - Design and coding required

Number of Pages Required

2 page

Font styles to use
Sans Serif

Colors
f04a50
3276b5
33a6d7

Requirements
Must have
• Simple and easy to use
• Ph number
• 4 web address; linked to page
• 0417385926
• tolvane.com.au
• tolvaneelectrical.com.au
• tolvaneairandelectrical.com.au
• tolvaneair.com.au
Nice to have
• Split System Air Con Picture
• Electrical Pictures

```html
<!DOCTYPE html>
<html lang="en">
<head>
<meta charset="utf-8">
<title>Tolvane Air and Electrical</title>
<link href="https://fonts.googleapis.com/css2?family=Exo+2:wght@400;500;600;700&family=Open+Sans:ital,wght@0,400;0,600;0,700;1,400&display=swap" rel="stylesheet">
<style>
:root{
  --red:#f04a50;
  --blue:#3276b5;
  --sky:#33a6d7;
  --ink:#1f1f1f;
  --text:#555;
  --grey-bg:#ececec;
  --dark:#262626;
  --white:#fff;
}
*{box-sizing:border-box;margin:0;padding:0}
html,body{width:1200px;height:3403px;overflow:hidden;background:var(--white)}
body{font-family:"Open Sans",Arial,sans-serif;color:var(--text);position:relative}
.abs{position:absolute}
a{color:inherit;text-decoration:none}
.heading{font-family:"Exo 2",Arial,sans-serif;font-weight:500;font-size:32px;text-align:center;color:var(--blue);letter-spacing:.5px}
.heading b{color:var(--red);font-weight:600}
.pill{display:inline-block;border-radius:30px;font-family:"Open Sans",sans-serif;font-weight:700;font-size:11px;letter-spacing:.5px;text-transform:uppercase;text-align:center}

/* hero */
.hero{top:0;left:0;width:1200px;height:560px;background:linear-gradient(180deg,#5b5148 0%,#7a6c5f 45%,#9b8f84 100%)}
.hero-shade{inset:0;background:rgba(20,20,20,.35)}
.brand{top:36px;left:86px;display:flex;align-items:center;gap:12px}
.brand-dot{width:44px;height:44px;border-radius:4px;background:var(--red)}
.brand-name{font-family:"Exo 2",sans-serif;font-weight:700;font-size:30px;color:var(--blue);letter-spacing:1px}
.brand-sub{display:none}
.top-phone{top:38px;left:622px;color:var(--blue);font-weight:700;font-size:15px}
.socials{top:32px;left:760px;display:flex;gap:10px}
.socials span{width:24px;height:24px;border:1.5px solid rgba(255,255,255,.7);border-radius:4px}
.quote-btn{top:32px;left:930px;width:182px;height:32px;line-height:32px;background:var(--blue);color:var(--white)}
.nav{top:92px;left:470px;display:flex;gap:40px;font-size:11.5px;font-weight:700;color:var(--white);letter-spacing:.5px}
.nav .active{color:var(--blue);border-bottom:2px solid var(--blue);padding-bottom:4px}
.hero-title{top:252px;left:0;width:1200px;text-align:center;font-family:"Exo 2",sans-serif;font-weight:600;font-size:33px;line-height:40px;color:var(--white);letter-spacing:1px}
.hero-cta{top:352px;left:536px;width:128px;height:32px;line-height:32px;background:var(--red);color:var(--white)}
.badge{top:500px;left:550px;width:100px;height:100px;border-radius:50%;background:var(--white);box-shadow:0 2px 8px rgba(0,0,0,.15)}

/* categories */
.cat-title{top:612px;left:0;width:1200px}
.cats{top:690px;left:90px;width:1020px;display:flex}
.cat{flex:1;height:120px;text-align:center;border-right:1px solid #e3e3e3;padding-top:10px}
.cat:last-child{border-right:none}
.cat svg{width:52px;height:52px}
.cat p{margin-top:12px;font-weight:700;font-size:14px;color:var(--ink)}
.arrow{color:#aaa;font-size:30px;line-height:1}

/* about */
.about{top:912px;left:0;width:1200px;height:400px;background:linear-gradient(90deg,#f2f2f2,#dcdcdc)}
.about-title{top:984px;left:88px;text-align:left}
.about-copy{top:1040px;left:88px;width:630px;font-size:12.5px;line-height:20px}
.about-copy p+p{margin-top:14px}
.discover{top:1208px;left:88px;width:144px;height:34px;line-height:34px;background:var(--blue);color:var(--white)}
.form{top:875px;left:835px;width:275px;height:486px;background:#f4f4f4;box-shadow:0 4px 14px rgba(0,0,0,.15)}
.form-head{height:110px;background:var(--blue);color:var(--white);font-family:"Exo 2",sans-serif;font-weight:600;font-size:26px;line-height:30px;text-align:center;padding-top:24px}
.form-body{padding:18px 22px}
.field{height:34px;background:var(--white);border:1px solid #ddd;margin-bottom:9px;font-size:11px;color:#aaa;padding:9px 10px}
.field.msg{height:96px}
.send{display:block;margin-top:14px;height:36px;line-height:36px;background:var(--red);color:var(--white)}

/* service cards */
.svc-title{top:1380px;left:0;width:1200px}
.cards{left:86px;width:1026px;display:flex;gap:32px}
.card{width:321px}
.photo{height:198px}
.card h3{margin-top:32px;font-size:17px;font-weight:700;color:var(--ink)}
.card ul{margin-top:18px;list-style:none;columns:2;font-size:11.5px;line-height:21px}
.card ul.one{columns:1}
.card ul li:before{content:"› ";color:#999}
.card p{margin-top:16px;font-size:11.5px;line-height:20px}
.more{display:block;margin-top:18px;font-size:10.5px;font-weight:700;color:var(--blue)}
.more.hot{color:var(--red)}

/* testimonials */
.testi{top:1916px;left:0;width:1200px;height:426px;background:linear-gradient(180deg,#3aa9dc,#2f9fd3)}
.testi-title{top:1984px;left:0;width:1200px;color:var(--white);font-family:"Exo 2",sans-serif;font-weight:600;font-size:30px;text-align:center}
.testi-quote{top:2048px;left:265px;width:670px;color:var(--white);font-style:italic;font-size:18px;line-height:28px;text-align:center}
.testi-date{top:2184px;left:0;width:1200px;text-align:center;color:var(--white);font-weight:700;font-size:12px}
.testi-who{top:2224px;left:0;width:1200px;text-align:center;color:var(--white);font-size:12.5px;line-height:22px}
.dots{top:2060px;left:1062px;display:flex;flex-direction:column;gap:8px}
.dots span{width:9px;height:9px;border-radius:50%;border:1.5px solid rgba(255,255,255,.8)}

/* breakdown */
.band{top:2858px;left:0;width:1200px;height:200px;background:var(--blue)}
.band-title{top:2912px;left:88px;color:var(--white);font-family:"Exo 2",sans-serif;font-weight:600;font-size:26px;letter-spacing:.5px}
.band-copy{top:2958px;left:88px;width:740px;color:var(--white);font-size:12px;line-height:20px}
.band-btn{top:2944px;left:982px;width:130px;height:34px;line-height:34px;background:var(--white);color:var(--blue)}

/* footer */
.footer{top:3057px;left:0;width:1200px;height:346px;background:var(--dark)}
.foot-brand{top:3150px;left:86px;display:flex;align-items:center;gap:12px}
.foot-brand .brand-name{font-size:34px}
.col{top:3118px;color:#ccc;font-size:11.5px;line-height:24px}
.col h4{color:var(--white);font-size:16px;font-weight:700;margin-bottom:10px}
.col .call{color:var(--blue);font-weight:700;font-size:15px}
.foot-social{display:flex;gap:10px;margin-top:6px}
.foot-social span{width:30px;height:30px;border-radius:50%;background:#666}
.foot-social span.on{background:var(--red)}
.up{top:3116px;left:1100px}
.divider{top:3334px;left:86px;width:1026px;height:1px;background:#444}
.copy{top:3360px;left:0;width:1200px;text-align:center;color:#aaa;font-size:11.5px}
.copy a{color:var(--blue)}
</style>
</head>
<body>

<header class="abs hero" role="img" aria-label="Photo of a woman relaxing on a couch with a split system air conditioner on a brick wall">
  <div class="abs hero-shade"></div>
</header>
<div class="abs brand"><span class="brand-dot"></span><span class="brand-name">TOLVANE</span></div>
<a class="abs top-phone" href="tel:0417385926">0417385926</a>
<div class="abs socials"><span></span><span></span><span></span><span></span></div>
<a class="abs pill quote-btn" href="#contact">Get a free quotes</a>
<nav class="abs nav">
  <a class="active" href="#">HOME</a><a href="#">ABOUT US</a><a href="#">SERVICES</a><a href="#">WHY US?</a><a href="#">TESTIMONIALS</a><a href="#">CONTACT US</a>
</nav>
<h1 class="abs hero-title">WE PROVIDE ELECTRICAL<br>AND AIR CONDITIONING SERVICES</h1>
<a class="abs pill hero-cta" href="#contact">Contact us</a>
<div class="abs badge"></div>

<h2 class="abs heading cat-title">SERVICE <b>CATEGORIES</b></h2>
<div class="abs arrow" style="top:738px;left:38px">‹</div>
<div class="abs arrow" style="top:738px;left:1148px">›</div>
<div class="abs cats">
  <div class="cat">
    <svg viewBox="0 0 52 52" fill="none" stroke-width="2"><rect x="6" y="12" width="40" height="16" rx="2" stroke="#3276b5"/><line x1="10" y1="23" x2="42" y2="23" stroke="#3276b5"/><path d="M16 34v8M26 34v10M36 34v8" stroke="#f04a50"/></svg>
    <p>Air Conditioning</p>
  </div>
  <div class="cat">
    <svg viewBox="0 0 52 52" fill="none" stroke-width="2"><circle cx="26" cy="26" r="20" stroke="#f04a50"/><path d="M20 16v8M32 16v8M16 24h20v6a10 10 0 0 1-20 0z" stroke="#3276b5"/></svg>
    <p>Electricians</p>
  </div>
  <div class="cat">
    <svg viewBox="0 0 52 52" fill="none" stroke-width="2"><rect x="8" y="8" width="36" height="36" rx="3" stroke="#3276b5"/><circle cx="26" cy="30" r="8" stroke="#f04a50"/><line x1="14" y1="16" x2="38" y2="16" stroke="#3276b5"/></svg>
    <p>Split System</p>
  </div>
  <div class="cat">
    <svg viewBox="0 0 52 52" fill="none" stroke-width="2"><circle cx="22" cy="22" r="9" stroke="#f04a50"/><circle cx="22" cy="22" r="3" stroke="#f04a50"/><circle cx="36" cy="36" r="6" stroke="#3276b5"/></svg>
    <p>Installation</p>
  </div>
  <div class="cat">
    <svg viewBox="0 0 52 52" fill="none" stroke-width="2"><rect x="16" y="6" width="20" height="40" rx="3" stroke="#3276b5"/><rect x="21" y="14" width="10" height="16" stroke="#f04a50"/></svg>
    <p>Safety Switches</p>
  </div>
</div>

<section class="abs about" role="img" aria-label="Faint photo of an electrician at work"></section>
<h2 class="abs heading about-title">ABOUT <b>US</b></h2>
<div class="abs about-copy">
  <p>With over 17 years' experience in the Electrical Industry, Tolvane Electrical provides a superior level of knowledge, a broad range of products and a high standard of customer service.</p>
  <p>To provide our customers with an immediate response within their timeframe, and deliver on-time, every time. Our friendly tradesmen are always professionally attired and treat your home or business with respect - we leave our jobs clean and tidy.</p>
</div>
<a class="abs pill discover" href="#">Discover more</a>

<form class="abs form" id="contact">
  <div class="form-head">Contact Us for<br>Free Quote</div>
  <div class="form-body">
    <div class="field">Name</div>
    <div class="field">Email</div>
    <div class="field">Phone</div>
    <div class="field">Service Requested</div>
    <div class="field msg">Message</div>
    <span class="pill send">➤ Send</span>
  </div>
</form>

<h2 class="abs heading svc-title">OUR <b>SERVICES</b></h2>
<div class="abs arrow" style="top:1535px;left:38px">‹</div>
<div class="abs arrow" style="top:1535px;left:1148px">›</div>
<div class="abs cards" style="top:1454px">
  <article class="card">
    <div class="photo" role="img" aria-label="Photo of an electrician fitting a chandelier" style="background:linear-gradient(135deg,#b6aa99,#5c5650)"></div>
    <h3>Domestic</h3>
    <ul><li>Mains</li><li>Switchboards</li><li>Lighting installation</li><li>General Electrical wiring installations</li><li>LED lighting</li><li>Fans and ventilation</li><li>Safety Switches</li></ul>
    <a class="more" href="#">READ MORE</a>
  </article>
  <article class="card">
    <div class="photo" role="img" aria-label="Photo of a modern commercial office interior" style="background:linear-gradient(135deg,#d8dcdf,#6b7074)"></div>
    <h3>Commercial</h3>
    <ul class="one"><li>Complete Office Fit Outs</li><li>Complete Retail &amp; Restaurant Fit Outs</li><li>Energy Efficient Lighting</li><li>Commercial Safety Switches</li></ul>
    <a class="more hot" href="#">READ MORE</a>
  </article>
  <article class="card">
    <div class="photo" role="img" aria-label="Photo of an electrician working on an industrial switchboard" style="background:linear-gradient(135deg,#8ea3b8,#4a5563)"></div>
    <h3>Industrial</h3>
    <ul class="one"><li>Three phase power</li><li>Switchboard upgrades and installation</li><li>Warehouse lighting</li><li>Industrial safety switches</li></ul>
    <a class="more" href="#">READ MORE</a>
  </article>
</div>

<section class="abs testi" role="img" aria-label="Blue tinted photo of electrical tools"></section>
<h2 class="abs testi-title">TESTIMONIALS</h2>
<p class="abs testi-quote">“ Excellent service. Marcus came and quoted at the agreed time. The team showed up on time an completed on time. Marcus and his guys were friendly and professional and I would highly recommend them. I will look to them for any future work. ”</p>
<p class="abs testi-date">10 MAY 2019</p>
<p class="abs testi-who"><b>Dana R, Westbrook, VIC</b><br>Split System Air Conditioning Verified Hired</p>
<div class="abs dots"><span></span><span></span><span></span><span></span></div>

<div class="abs arrow" style="top:2503px;left:38px">‹</div>
<div class="abs arrow" style="top:2503px;left:1148px">›</div>
<div class="abs cards" style="top:2422px">
  <article class="card">
    <div class="photo" role="img" aria-label="Photo of an electrician fitting a chandelier" style="background:linear-gradient(135deg,#b6aa99,#5c5650)"></div>
    <h3>Why Us?</h3>
    <p>On Time We arrive on time. If there is an unavoidable delay we'll call ahead to let you know when we'll be there ...</p>
    <a class="more" href="#">READ MORE</a>
  </article>
  <article class="card">
    <div class="photo" role="img" aria-label="Photo of a modern commercial office interior" style="background:linear-gradient(135deg,#d8dcdf,#6b7074)"></div>
    <h3>Quality</h3>
    <p>We are committed to best practice electrical safety standards and highest quality performance on the job ...</p>
    <a class="more hot" href="#">READ MORE</a>
  </article>
  <article class="card">
    <div class="photo" role="img" aria-label="Photo of an electrician working on an industrial switchboard" style="background:linear-gradient(135deg,#8ea3b8,#4a5563)"></div>
    <h3>Price</h3>
    <p>Price is always important and our standard rates are competitive. Where jobs require an individual...</p>
    <a class="more" href="#">READ MORE</a>
  </article>
</div>

<section class="abs band"></section>
<h2 class="abs band-title">24HR BREAKDOWN &amp; REPAIR SERVICE</h2>
<p class="abs band-copy">Tolvane Electrical has a qualified electrician standing by with a fully stocked truck to assist you and your electrical needs around the clock. 24 hour emergency electrical services for your convenience.</p>
<a class="abs pill band-btn" href="#contact">Contact us</a>

<footer class="abs footer"></footer>
<div class="abs foot-brand"><span class="brand-name">TOLVANE</span></div>
<div class="abs col" style="left:374px">
  <h4>Quick Links</h4>
  About US<br>Services<br>Why Us?<br>Testimonials<br>Suburbs Serviced<br>Contact Us
</div>
<div class="abs col" style="left:583px">
  <h4>Contact Us</h4>
  <span class="call">CALL US ✆ 0417385926</span><br>
  info@tolvaneairandelectrical.com.au<br>
  <span style="display:block;margin-top:10px;color:#fff;font-weight:700">Address:</span>
  <span style="display:block;line-height:20px">Marcus Tolvane, Elmridge<br>VIC 3199</span>
</div>
<div class="abs col" style="left:880px">
  <h4>Follow Us</h4>
  <div class="foot-social"><span></span><span class="on"></span><span></span><span></span></div>
</div>
<svg class="abs up" width="20" height="20" viewBox="0 0 20 20" fill="none" stroke="#3276b5" stroke-width="2"><path d="M3 17L10 3l7 14"/></svg>
<div class="abs divider"></div>
<p class="abs copy">© 2019 <a href="#">Tolvane Air and Electrical</a> All Right Reserved</p>

</body>
</html>
```